Bref créative
Corvane Oral Care Stationary
Corvane Oral Care
Professional
R. Lucien Dorvash, DDS, MAGD
2483 W Perrin Ave.
Baytown, TX 77520
dentist@qbl.zx.com
www.corvaneoralcare.com

```html
<!DOCTYPE html>
<html lang="en">
<head>
<meta charset="utf-8">
<title>Corvane Oral Care – Business Card</title>
<link rel="stylesheet" href="https://fonts.googleapis.com/css2?family=Tinos:wght@400;700&display=swap">
<style>
  :root {
    --paper: #ffffff;
    --ink: #1c1c1c;
    --brand-grey: #7d838b;
    --brand-teal: #9fd3cf;
    --band-blue: #3f4f9c;
    --band-green: #86c240;
    --on-band: #ffffff;
  }
  * { margin: 0; padding: 0; box-sizing: border-box; }
  html, body { width: 1200px; height: 686px; overflow: hidden; background: var(--paper); }
  .card {
    position: relative;
    width: 1200px;
    height: 686px;
    background: var(--paper);
    font-family: "Tinos", "Times New Roman", serif;
    color: var(--ink);
    overflow: hidden;
  }
  .footer-band {
    position: absolute;
    left: 0;
    top: 470px;
    width: 1200px;
    height: 216px;
    background: linear-gradient(90deg, var(--band-blue) 0%, #6f9f55 28%, var(--band-green) 50%, #6f9f55 75%, var(--band-blue) 100%);
  }
  .brand-mark {
    position: absolute;
    left: 249px;
    top: 70px;
    width: 150px;
    height: 150px;
    border-radius: 50%;
    background: var(--brand-teal);
  }
  .brand-name {
    position: absolute;
    left: 124px;
    top: 300px;
    width: 400px;
    text-align: center;
    font-weight: 700;
    font-size: 40px;
    line-height: 1.1;
    color: var(--brand-grey);
    white-space: nowrap;
  }
  .doctor {
    position: absolute;
    right: 38px;
    top: 230px;
    text-align: right;
  }
  .doctor-name { font-weight: 700; font-size: 31px; line-height: 40px; }
  .doctor-title { font-size: 30px; line-height: 40px; }
  .address {
    position: absolute;
    left: 43px;
    top: 568px;
    color: var(--on-band);
    font-style: normal;
    font-size: 26px;
    line-height: 36px;
  }
  .contact {
    position: absolute;
    right: 38px;
    top: 520px;
    color: var(--on-band);
    font-size: 25px;
    line-height: 35px;
    text-align: right;
  }
</style>
</head>
<body>
<main class="card">
  <div class="footer-band" role="img" aria-label="Decorative blue and green footer band"></div>

  <div class="brand-mark"></div>
  <div class="brand-name">Corvane Oral Care</div>

  <div class="doctor">
    <div class="doctor-name">R. Lucien Dorvash</div>
    <div class="doctor-title">DDS, MAGD</div>
  </div>

  <address class="address">
    2483 W Perrin Ave.<br>
    Baytown, TX 77520
  </address>

  <div class="contact">
    Phone : 281-555-0142<br>
    Fax : 281-555-0187<br>
    Email : dentist@qbl.zx.com<br>
    Web : www.corvaneoralcare.com
  </div>
</main>
</body>
</html>
```